Business card for new consulting business - Brenvale Holdings Pty Ltd.

Consulting in the areas of Occupational Health, Safety and Community Relations in the resources (mining) industries. The consultant (me) will work both within Australia and overseas jurisdictions such as South East Asia, Africa , South America etc, often working with third world indigenous communities. The design should suggest a high level of social and environmental responsibility.

```html
<!DOCTYPE html>
<html lang="en">
<head>
<meta charset="utf-8">
<title>Brenvale Holdings Pty Ltd — Business Card</title>
<link href="https://fonts.googleapis.com/css2?family=Exo+2:wght@600&family=Lato:wght@400&display=swap" rel="stylesheet">
<style>
  :root {
    --bg: #1c1c1d;
    --card: #2a2a2b;
    --card-edge: #232324;
    --blue: #1a7fd4;
    --blue-bright: #2a8ee6;
    --white: #f2f2f2;
    --emboss: #4a4a4c;
    --emboss-light: #6b6b6e;
  }
  * { margin: 0; padding: 0; box-sizing: border-box; }
  html, body {
    width: 1200px; height: 900px; overflow: hidden;
    background: var(--bg);
  }
  .canvas {
    width: 1200px; height: 900px;
    display: flex; flex-direction: column; align-items: center;
    justify-content: center; gap: 36px;
  }
  .card {
    position: relative;
    width: 700px; height: 396px;
    background: linear-gradient(135deg, var(--card-edge) 0%, var(--card) 55%, #303032 100%);
    box-shadow: 0 10px 30px rgba(0,0,0,.55);
    overflow: hidden;
  }
  .card::after {
    content: ""; position: absolute; left: 0; right: 0; bottom: 0;
    height: 7px; background: var(--blue);
  }
  /* front */
  .card--front {
    display: flex; align-items: center; justify-content: center;
  }
  .brand {
    display: flex; align-items: center; gap: 18px;
    font-family: "Exo 2", sans-serif; font-weight: 600;
  }
  .brand__mark { width: 34px; height: 34px; flex: none; }
  .brand__name { line-height: 1.05; }
  .card--front .brand__name {
    font-size: 40px; color: var(--emboss);
    text-shadow: 0 1px 0 rgba(255,255,255,.08);
  }
  .card--front .brand__mark { background: var(--emboss); }
  /* back */
  .card--back { display: flex; align-items: center; }
  .back__brand {
    width: 340px; padding-left: 48px;
  }
  .card--back .brand { gap: 14px; }
  .card--back .brand__name { font-size: 29px; color: var(--blue-bright); }
  .card--back .brand__mark { width: 26px; height: 26px; background: var(--blue-bright); }
  .divider {
    width: 2px; height: 212px; background: var(--blue); flex: none;
  }
  .contact {
    padding-left: 34px;
    font-family: "Lato", sans-serif; color: var(--white);
  }
  .contact__name {
    font-family: "Exo 2", sans-serif; font-weight: 600;
    font-size: 34px; color: var(--blue-bright); line-height: 1;
  }
  .contact__role { font-size: 18px; margin-top: 4px; }
  .contact__address { font-size: 18px; line-height: 1.3; margin-top: 18px; }
  .contact__lines { list-style: none; margin-top: 12px; font-size: 18px; line-height: 1.45; }
  .contact__lines li { display: flex; align-items: center; gap: 10px; }
  .contact__lines svg { width: 15px; height: 15px; flex: none; }
  .accent { color: var(--blue-bright); }
</style>
</head>
<body>
<main class="canvas">
  <section class="card card--front" aria-label="Card front">
    <div class="brand">
      <span class="brand__mark"></span>
      <span class="brand__name">Brenvale Holdings Pty Ltd</span>
    </div>
  </section>

  <section class="card card--back" aria-label="Card back">
    <div class="back__brand">
      <div class="brand">
        <span class="brand__mark"></span>
        <span class="brand__name">Brenvale Holdings<br>Pty Ltd</span>
      </div>
    </div>
    <div class="divider"></div>
    <div class="contact">
      <h1 class="contact__name">Dana Whitlock</h1>
      <p class="contact__role">Founder</p>
      <p class="contact__address">48 Harrow Lane<br>Kestrel Bay, QLD 4870</p>
      <ul class="contact__lines">
        <li>
          <svg viewBox="0 0 24 24" fill="none" stroke="#1a7fd4" stroke-width="2"><path d="M5 3h4l2 5-3 2a11 11 0 0 0 6 6l2-3 5 2v4a2 2 0 0 1-2 2A17 17 0 0 1 3 5a2 2 0 0 1 2-2z"/></svg>
          07 5550 3184
        </li>
        <li>
          <svg viewBox="0 0 24 24" fill="none" stroke="#1a7fd4" stroke-width="2"><rect x="3" y="6" width="18" height="12" rx="1"/><path d="M3 7l9 6 9-6"/></svg>
          info@brenvaleholdings.com
        </li>
        <li>
          <svg viewBox="0 0 24 24" fill="none" stroke="#1a7fd4" stroke-width="2"><circle cx="12" cy="12" r="9"/><path d="M3 12h18M12 3c3 3 3 15 0 18M12 3c-3 3-3 15 0 18"/></svg>
          <span>www.<span class="accent">brenvaleholdings</span>.com</span>
        </li>
      </ul>
    </div>
  </section>
</main>
</body>
</html>
```